Business Card design

We have found an idea we would like to do something similar.
We would require the cards for the inside and the wrapping sheet for the outside, you will see what I mean when you see the image attached. (gum packet) The company is called.... Quillgate Swift Press
I will include the company logo also.
If you could create the outside wrapping with the ability to have staff members name and mobile, maybe on one side panel we would have the address, the other side would be phone numbers, the front would be staff members name and mobile number and email. The other side would be company name and logo if it fits, the logo could wrap around if needed. Open to all ideas.

```html
<!DOCTYPE html>
<html lang="en">
<head>
<meta charset="utf-8">
<title>Quillgate Swift Press – Wrapper Card</title>
<link href="https://fonts.googleapis.com/css2?family=Arvo:wght@700&family=Arimo:wght@400;700&display=swap" rel="stylesheet">
<style>
  :root {
    --page: #ececec;
    --paper: #e9e5cf;
    --paper-edge: #d9d4b8;
    --orange: #e0702a;
    --red: #b8231f;
    --ink: #2f2f2f;
    --ink-soft: #3a3a3a;
    --rule: #4a4a4a;
    --mark-orange: #e9832f;
  }
  * { box-sizing: border-box; margin: 0; padding: 0; }
  html, body { width: 1200px; height: 1200px; overflow: hidden; }
  body {
    background: var(--page);
    font-family: "Arimo", Arial, sans-serif;
    color: var(--ink);
    position: relative;
  }
  .wrapper-face {
    position: absolute;
    left: 100px;
    width: 1000px;
    height: 440px;
    background: var(--paper);
    border: 1px solid var(--paper-edge);
    box-shadow: 0 6px 18px rgba(0,0,0,0.12);
  }
  .face-front { top: 90px; }
  .face-back { top: 650px; }

  /* Front face */
  .title-band {
    position: absolute;
    left: 0; right: 0; top: 36px;
    height: 84px;
    border-top: 2px solid var(--rule);
    border-bottom: 2px solid var(--rule);
    display: flex; align-items: center; justify-content: center;
  }
  .company-title {
    font-family: "Arvo", Georgia, serif;
    font-weight: 700;
    font-size: 54px;
    letter-spacing: 1px;
    color: var(--orange);
    text-transform: uppercase;
  }
  .staff-name {
    position: absolute; left: 60px; top: 150px;
    font-family: "Arvo", Georgia, serif;
    font-weight: 700;
    font-size: 40px;
    color: var(--ink);
    text-transform: uppercase;
  }
  .staff-role {
    position: absolute; left: 60px; top: 200px;
    font-size: 28px;
    color: var(--ink-soft);
  }
  .brand-lockup {
    position: absolute;
    display: flex; align-items: center;
  }
  .front-lockup { left: 60px; top: 270px; gap: 18px; }
  .brand-dot {
    border-radius: 50%;
    background: var(--mark-orange);
    flex: none;
  }
  .front-lockup .brand-dot { width: 64px; height: 64px; }
  .brand-name {
    font-family: "Arimo", Arial, sans-serif;
    font-weight: 400;
    color: var(--ink);
    line-height: 1.05;
  }
  .front-lockup .brand-name { font-size: 30px; }
  .contact-block {
    position: absolute; left: 560px; top: 160px;
    font-size: 32px;
    line-height: 1.35;
  }
  .contact-block .phone { font-weight: 700; }
  .address-line {
    position: absolute; left: 520px; top: 370px;
    font-size: 24px;
    color: var(--ink);
  }

  /* Back face */
  .back-lockup { left: 110px; top: 60px; gap: 40px; }
  .back-lockup .brand-dot { width: 190px; height: 190px; }
  .back-lockup .brand-name { font-size: 70px; }
  .side-band {
    position: absolute;
    left: 0; right: 0; bottom: 40px;
    height: 88px;
    border-top: 2px solid var(--rule);
    border-bottom: 2px solid var(--rule);
    display: flex; align-items: center; justify-content: center;
  }
  .side-band .company-title { color: var(--red); }
</style>
</head>
<body>
  <section class="wrapper-face face-front" aria-label="Front panel">
    <div class="title-band"><span class="company-title">Quillgate Swift Press</span></div>
    <div class="staff-name">Daniel Hartley</div>
    <div class="staff-role">Manager</div>
    <div class="brand-lockup front-lockup">
      <span class="brand-dot"></span>
      <span class="brand-name">Quillgate<br>Swift Press</span>
    </div>
    <div class="contact-block">
      <div class="phone">P: 123-555-0148</div>
      <div class="email">yourname@quillgatemail.com</div>
    </div>
    <div class="address-line">Your address, city, state, ZIP 0000</div>
  </section>

  <section class="wrapper-face face-back" aria-label="Back panel">
    <div class="brand-lockup back-lockup">
      <span class="brand-dot"></span>
      <span class="brand-name">Quillgate<br>Swift Press</span>
    </div>
    <div class="side-band"><span class="company-title">Quillgate Swift Press</span></div>
  </section>
</body>
</html>
```